Poster Design Project - Front Window Poster for IT Business

Design a poster to be displayed in the front window of our office.
To include the following text:
Brightlane Systems Group
Servers & Networks
Deskora 720
Cloud Solutions
Helpdesk Services & Support
Network Audits
Disaster Recovery
IT Consulting
Contact details to be shown on the poster:
www.tk.com.au
02 5183 6214
Please also include the logo and related colour scheme.
Needs to look professional and easy to read from the street.
Must be in A1 format, printable through prontoleaf.

```html
<!DOCTYPE html>
<html lang="en">
<head>
<meta charset="utf-8">
<title>TK Technology Solutions – Window Poster</title>
<link href="https://fonts.googleapis.com/css2?family=Arimo:wght@400;700&family=Tinos&display=swap" rel="stylesheet">
<style>
  :root {
    --bullet: #1fd0f5;
    --royal: #4a6fd6;
    --navy: #1c3f94;
    --ink: #111111;
    --paper: #ffffff;
    --haze: #edf4fd;
  }
  html, body {
    margin: 0;
    padding: 0;
    width: 854px;
    height: 1200px;
    overflow: hidden;
    background: var(--paper);
  }
  .poster {
    position: relative;
    width: 854px;
    height: 1200px;
    overflow: hidden;
    background: var(--paper);
  }
  .backdrop {
    position: absolute;
    left: 0;
    top: 295px;
    width: 854px;
    height: 905px;
    background: linear-gradient(160deg, var(--haze) 0%, #f4f8fe 55%, var(--paper) 100%);
  }
  .company-name {
    position: absolute;
    left: 0;
    top: 78px;
    width: 854px;
    margin: 0;
    text-align: center;
    font: 700 74px/88px "Arimo", sans-serif;
    color: var(--navy);
  }
  .company-name span { display: block; }
  .services {
    position: absolute;
    left: 133px;
    top: 317px;
    margin: 0;
    padding: 0;
    list-style: none;
  }
  .services li {
    position: relative;
    height: 89.3px;
    padding-left: 34px;
    font: 400 45.5px/52px "Arimo", sans-serif;
    color: var(--ink);
    white-space: nowrap;
  }
  .services li::before {
    content: "";
    position: absolute;
    left: 0;
    top: 18px;
    width: 17px;
    height: 17px;
    background: var(--bullet);
  }
  .contact {
    position: absolute;
    left: 128px;
    top: 1056px;
    margin: 0;
    padding: 0;
    list-style: none;
  }
  .contact li {
    display: flex;
    align-items: center;
    height: 58px;
    font: 400 27px/1 "Tinos", serif;
    color: var(--navy);
  }
  .contact svg {
    width: 26px;
    height: 26px;
    margin-right: 14px;
    flex: none;
  }
  .signoff {
    position: absolute;
    right: 34px;
    top: 1090px;
    display: flex;
    align-items: center;
    gap: 12px;
  }
  .signoff-square {
    width: 18px;
    height: 18px;
    background: var(--bullet);
  }
  .signoff-name {
    margin: 0;
    font: 700 22px/1.15 "Arimo", sans-serif;
    color: var(--navy);
  }
</style>
</head>
<body>
  <main class="poster">
    <div class="backdrop" role="img" aria-label="Soft pale blue background panel behind the service list"></div>

    <h1 class="company-name"><span>TK Technology</span><span>Solutions</span></h1>

    <ul class="services">
      <li>Brightlane Systems Group</li>
      <li>Servers &amp; Networks</li>
      <li>Deskora 720</li>
      <li>Cloud Solutions</li>
      <li>Helpdesk Services &amp; Support</li>
      <li>Network Audits</li>
      <li>Disaster Recovery</li>
      <li>IT Consulting</li>
    </ul>

    <ul class="contact">
      <li>
        <svg viewBox="0 0 24 24" aria-hidden="true">
          <path d="M12 2 1 12h3v10h6v-6h4v6h6V12h3z" fill="var(--bullet)"/>
        </svg>
        www.tk.com.au
      </li>
      <li>
        <svg viewBox="0 0 24 24" aria-hidden="true">
          <rect x="1" y="3" width="22" height="5" rx="1" fill="var(--bullet)"/>
          <rect x="3" y="9" width="18" height="14" fill="var(--bullet)"/>
          <g fill="var(--paper)">
            <rect x="6" y="12" width="3" height="2"/><rect x="10.5" y="12" width="3" height="2"/><rect x="15" y="12" width="3" height="2"/>
            <rect x="6" y="16" width="3" height="2"/><rect x="10.5" y="16" width="3" height="2"/><rect x="15" y="16" width="3" height="2"/>
          </g>
        </svg>
        02 5183 6214
      </li>
    </ul>

    <div class="signoff">
      <span class="signoff-square" aria-hidden="true"></span>
      <p class="signoff-name">TK Technology<br>Solutions</p>
    </div>
  </main>
</body>
</html>
```